Victorian-Inspired Body Lotion Labels, Room Spray Labels (Total of 8 Coordinated Labels)

We need labels for a victorian-inspired home and body care brand. We have existing products that we need to match. We'd like to see vintage-inspired labels, possible use of black and white stripes, and the final label should have a sophisticated, whimsical style, and communicate luxury home and body care.

The room spray label should coordinate with our candle labels. 3 sizes needed: 2oz, 4oz, and 8oz.

The body lotion label should complement our candle and room spray labels. 5 sizes needed in varying shapes: 8.5 oz Roma Bottle, and 16oz and 32oz boston round, 1oz, and 4oz sample pots.

We sell online, in stores, and at markets. The products need to look good on all 3 sales channels.

Label Sizes -

Lotion (AMBER COLOR Glass) - 5 Labels

>>Roma Bottle - 2.85"H x 1.9"W (https://www.vialcrest.com/8-5-oz-tavo-glass-bottle-28mm-thread/)
>>16oz Boston Round (https://www.quillvesselco.com/7312k42-kqrt-tall-round-glass-bottles-16-oz-amber-case-of-12/)
>>32oz Boston Round (https://www.quillvesselco.com/7312k44-kqrt-tall-round-glass-bottles-32-oz-amber-case-of-12/)
>>1oz squat jar: https://www.quillvesselco.com/8204k63-k-1-oz-amber-glass-straight-sided-squat-jars-cap-not-included/
>>4oz squat jar: https://www.quillvesselco.com/4-oz-amber-glass-straight-sided-squat-jars-cap-not-included-8204k68/

ROOM SPRAY (3 Labels) - White Frosted Bottles with Black Spray Tops

>>2oz Frosted White Glass: https://www.flaskandtin.com/products/glass-tall-round/K419RTW
>>4oz Frosted White Glass: https://www.flaskandtin.com/products/glass-tall-round/K402RTWB
>>8oz (https://www.flaskandtin.com/products/glass-tall-round/K1308RTW)

Inspiration Board: https://www.pinterest.com/dovwellsbury/lotion-labels/

Label Info Needed:

Lotion Labels Need to Have:
Body Lotion
Made with Avocado Oil, Shea Butter, and Coconut Oil
The Gilded Wickery
Logo
Scent
ml/ounces

Room Spray Labels Need to Have:
The Gilded Wickery
Logo
Scent Name
Scent Note | Scent Note | Scent Note
Artisinal Room Spray
ml/ounces

Target Market(s)

Women and Men 25-35, Women 35-75, upscale, mid-high income

Industry/Entity Type

Handmade home and body goods

Font styles to use
Other font styles liked:
• Lora, Cinzel, Cinzel Decorative

Requirements
Must have
• Room spray must coordinate with existing candle labels, body lotion labels must all coordinate with each other
Nice to have
• Black and white vertical stripes

```html
<!DOCTYPE html>
<html lang="en">
<head>
<meta charset="utf-8">
<title>The Gilded Wickery — Label Set</title>
<link href="https://fonts.googleapis.com/css2?family=Cinzel:wght@600&family=Oswald:wght@500&family=Lato:wght@400&display=swap" rel="stylesheet">
<style>
  :root {
    --ink: #1c1c1c;
    --ink-soft: #2b2b2b;
    --paper: #f7f7f7;
    --paper-shade: #ececec;
    --rule-dark: #8a8a8a;
    --rule-light: #9a9a9a;
    --text-light: #f2f2f2;
    --text-mid: #cfcfcf;
    --text-dark: #2a2a2a;
    --bg-top: #f6f6f6;
    --bg-bottom: #e4e4e4;
  }
  * { box-sizing: border-box; margin: 0; padding: 0; }
  html, body { width: 1200px; height: 900px; overflow: hidden; }
  body {
    position: relative;
    background: linear-gradient(180deg, var(--bg-top) 0%, var(--bg-bottom) 100%);
    font-family: "Lato", Arial, sans-serif;
  }
  .label { position: absolute; display: flex; flex-direction: column; box-shadow: 0 2px 6px rgba(0,0,0,0.08); }
  .label-spray { left: 302px; top: 473px; width: 190px; height: 232px; }
  .label-lotion { left: 602px; top: 317px; width: 290px; height: 379px; }

  .panel { position: relative; display: flex; flex-direction: column; align-items: center; }
  .panel-light { background: linear-gradient(180deg, var(--paper) 0%, var(--paper-shade) 100%); color: var(--text-dark); }
  .panel-dark { background: linear-gradient(180deg, var(--ink-soft) 0%, var(--ink) 100%); color: var(--text-light); }

  .label-spray .panel-brand { height: 49%; justify-content: center; }
  .label-spray .panel-info { height: 51%; padding-top: 11px; }
  .label-lotion .panel-brand { height: 49%; justify-content: center; }
  .label-lotion .panel-info { height: 51%; padding-top: 18px; }

  .brand-mark { display: flex; flex-direction: column; align-items: center; gap: 7px; }
  .brand-dot { width: 9px; height: 9px; border-radius: 50%; }
  .panel-light .brand-dot { background: var(--text-dark); }
  .panel-dark .brand-dot { background: var(--text-light); }
  .brand-name {
    font-family: "Cinzel", Georgia, serif;
    font-weight: 600;
    text-align: center;
    line-height: 1.05;
    letter-spacing: 0.02em;
  }
  .label-spray .brand-name { font-size: 15px; }
  .label-lotion .brand-name { font-size: 24px; }

  .info-box {
    display: flex; flex-direction: column; align-items: center;
    border: 1px solid var(--rule-dark);
  }
  .panel-light .info-box { border-color: var(--rule-light); }
  .label-spray .info-box { width: 124px; padding: 7px 4px 3px; }
  .label-lotion .info-box { width: 194px; padding: 13px 8px 10px; }

  .product-title { font-family: "Oswald", "Arial Narrow", sans-serif; font-weight: 500; letter-spacing: 0.02em; white-space: nowrap; }
  .label-spray .product-title { font-size: 10.5px; }
  .label-lotion .product-title { font-size: 17px; }

  .rule { width: 88%; height: 1px; background: var(--rule-dark); }
  .label-spray .rule { margin: 4px 0 3px; }
  .label-lotion .rule { margin: 8px 0 4px; }

  .scent-name { letter-spacing: 0.02em; white-space: nowrap; }
  .label-spray .scent-name { font-size: 7px; color: var(--text-mid); }
  .label-lotion .scent-name { font-size: 9.5px; }

  .scent-notes { display: flex; width: 100%; margin-top: 2px; }
  .scent-note {
    flex: 1; text-align: center; font-size: 4.5px; color: var(--text-mid);
    padding: 2px 0; letter-spacing: 0.02em; white-space: nowrap;
  }
  .scent-note + .scent-note { border-left: 1px solid var(--rule-dark); }

  .ingredients { font-size: 6px; text-align: center; line-height: 1.35; margin-top: 3px; letter-spacing: 0.02em; }

  .flourish-area { border-radius: 3px; margin-top: auto; }
  .panel-dark .flourish-area { background: #4a4a4a; }
  .panel-light .flourish-area { background: #b8b8b8; }
  .label-spray .flourish-area { width: 28px; height: 4px; }
  .label-lotion .flourish-area { width: 46px; height: 6px; }

  .net-weight { color: inherit; opacity: 0.75; }
  .label-spray .net-weight { font-size: 4.5px; margin: 3px 0 9px; }
  .label-lotion .net-weight { font-size: 5.5px; margin: 4px 0 24px; }
</style>
</head>
<body>

  <section class="label label-spray" aria-label="Artisinal room spray label">
    <div class="panel panel-light panel-brand">
      <div class="brand-mark">
        <span class="brand-dot"></span>
        <p class="brand-name">The Gilded<br>Wickery</p>
      </div>
    </div>
    <div class="panel panel-dark panel-info">
      <div class="info-box">
        <h2 class="product-title">ARTISINAL ROOM SPRAY</h2>
        <div class="rule"></div>
        <p class="scent-name">AMBER ORCHARD</p>
        <div class="rule"></div>
        <div class="scent-notes">
          <span class="scent-note">SCENT NOTE</span>
          <span class="scent-note">SCENT NOTE</span>
          <span class="scent-note">SCENT NOTE</span>
        </div>
      </div>
      <div class="flourish-area" role="img" aria-label="Small decorative flourish divider"></div>
      <p class="net-weight">Weight 8 oz</p>
    </div>
  </section>

  <section class="label label-lotion" aria-label="Body lotion label">
    <div class="panel panel-dark panel-brand">
      <div class="brand-mark">
        <span class="brand-dot"></span>
        <p class="brand-name">The Gilded<br>Wickery</p>
      </div>
    </div>
    <div class="panel panel-light panel-info">
      <div class="info-box">
        <h2 class="product-title">BODY LOTION</h2>
        <div class="rule"></div>
        <p class="scent-name">AMBER ORCHARD</p>
        <div class="rule"></div>
        <p class="ingredients">MADE WITH AVOCADO OIL, SHEA BUTTER,<br>AND COCONUT OIL</p>
      </div>
      <div class="flourish-area" role="img" aria-label="Small decorative flourish divider"></div>
      <p class="net-weight">Weight 32 oz</p>
    </div>
  </section>

</body>
</html>
```